KRV e-payment Business Card Design

We require a new business card design to suit our expanding consulting business -who are specialists in 2 main areas
1. Advising large Corporations and Government organisation on how to improve the why they use emerging (B2B) electronic payment systems
2. Educate Global and regional banks on how to design, build and market electronic business payment products in emerging markets

Our logo is grey/silver based with a building block theme. It also suggests "insight" and business know-how capitalizing on our KRV name. We also want to engender trust,security and balance via the ying/yan symbol

The design needs to take into account the target regional areas of Australiasia/Asia Pacific/Middle East and Africa

Target Market(s)

Regional Banks and their business customers

Industry/Entity Type

Electronic

Contact Information for Business Card

Marcus Delwyn
Director KRV Consulting (Aust) Pty Ltd
PO Box 7463
Brookvale NSW 2175
Australia
tel +61 (0) 2 95550417
mob +61 (0) 455503862
krvconsulting@tallwire.example

```html
<!DOCTYPE html>
<html lang="en">
<head>
<meta charset="utf-8">
<title>KRV Consulting – Business Card</title>
<link rel="stylesheet" href="https://fonts.googleapis.com/css2?family=Source+Sans+3:wght@400;500&display=swap">
<style>
  :root {
    --backdrop: #3c3c3c;
    --card-white: #ffffff;
    --card-top-tint: #ececec;
    --brand-blue: #175c98;
    --name-blue: #1f79c2;
    --tagline-grey: #555555;
    --title-black: #111111;
    --band-light: #22a6df;
    --band-mid: #2a3f98;
    --band-dark: #121045;
    --band-rim: #3a3a3a;
    --contact-white: #ffffff;
    --mark-dark: #111111;
  }
  * { margin: 0; padding: 0; box-sizing: border-box; }
  html, body {
    width: 1200px;
    height: 999px;
    overflow: hidden;
  }
  body {
    background: var(--backdrop);
    font-family: "Source Sans 3", "Myriad Pro", sans-serif;
    position: relative;
  }
  .business-card {
    position: absolute;
    left: 75px;
    top: 200px;
    width: 1050px;
    height: 599px;
    background: linear-gradient(to bottom, var(--card-top-tint) 0, var(--card-white) 70px);
    overflow: hidden;
  }
  .brand {
    position: absolute;
    left: 328px;
    top: 55px;
    display: flex;
    align-items: center;
    gap: 18px;
  }
  .brand-dot {
    width: 126px;
    height: 126px;
    border-radius: 50%;
    background: var(--mark-dark);
  }
  .brand-name {
    font-weight: 400;
    font-size: 142px;
    line-height: 1;
    color: var(--brand-blue);
    letter-spacing: -2px;
  }
  .company-line {
    position: absolute;
    left: 0;
    width: 1056px;
    top: 192px;
    text-align: center;
    font-size: 33px;
    color: var(--tagline-grey);
  }
  .person-name {
    position: absolute;
    left: 0;
    width: 1040px;
    top: 270px;
    text-align: center;
    font-size: 45px;
    color: var(--name-blue);
  }
  .person-title {
    position: absolute;
    left: 0;
    width: 1050px;
    top: 330px;
    text-align: center;
    font-size: 25px;
    color: var(--title-black);
  }
  .contact-band {
    position: absolute;
    left: 0;
    top: 370px;
    width: 1050px;
    height: 229px;
  }
  .contact-block {
    position: absolute;
    color: var(--contact-white);
    font-size: 26px;
    line-height: 35px;
  }
  .contact-address { left: 95px; top: 462px; }
  .contact-lines { left: 635px; top: 458px; }
  .contact-row { display: flex; align-items: center; gap: 24px; }
  .contact-icon { width: 24px; height: 24px; flex: none; }
  .pin-icon {
    position: absolute;
    left: 43px;
    top: 470px;
    width: 24px;
    height: 36px;
  }
</style>
</head>
<body>
  <div class="business-card">
    <div class="brand">
      <div class="brand-dot"></div>
      <div class="brand-name">KRV</div>
    </div>
    <div class="company-line">Consulting (Aust) Pty Ltd.</div>
    <div class="person-name">Marcus Delwyn</div>
    <div class="person-title">Director</div>

    <svg class="contact-band" viewBox="0 0 1050 229" preserveAspectRatio="none" aria-hidden="true">
      <defs>
        <linearGradient id="bandFill" x1="0" y1="0" x2="0" y2="1">
          <stop offset="0" stop-color="var(--band-light)"/>
          <stop offset="0.45" stop-color="var(--band-mid)"/>
          <stop offset="1" stop-color="var(--band-dark)"/>
        </linearGradient>
      </defs>
      <path d="M0 52 Q525 -25 1050 56 L1050 229 L0 229 Z" fill="url(#bandFill)"/>
      <path d="M0 52 Q525 -25 1050 56" fill="none" stroke="var(--band-rim)" stroke-width="7"/>
    </svg>

    <svg class="pin-icon" viewBox="0 0 24 36" aria-hidden="true">
      <path d="M12 0C5.4 0 0 5.3 0 11.8 0 20 12 36 12 36s12-16 12-24.2C24 5.3 18.6 0 12 0zm0 16.5a4.8 4.8 0 1 1 0-9.6 4.8 4.8 0 0 1 0 9.6z" fill="#fff"/>
    </svg>
    <div class="contact-block contact-address">
      <div>(Aust) Pty Ltd PO Box 7463</div>
      <div>Brookvale NSW 2175</div>
      <div>Australia</div>
    </div>

    <div class="contact-block contact-lines">
      <div class="contact-row">
        <svg class="contact-icon" viewBox="0 0 24 24" aria-hidden="true">
          <path d="M6.6 10.8a15.1 15.1 0 0 0 6.6 6.6l2.2-2.2c.3-.3.7-.4 1-.2 1.1.4 2.3.6 3.6.6.6 0 1 .4 1 1V20c0 .6-.4 1-1 1C10.6 21 3 13.4 3 4c0-.6.4-1 1-1h3.5c.6 0 1 .4 1 1 0 1.3.2 2.5.6 3.6.1.3 0 .7-.2 1z" fill="#fff"/>
          <path d="M14 3a7 7 0 0 1 7 7M14 6.5a3.5 3.5 0 0 1 3.5 3.5" fill="none" stroke="#fff" stroke-width="1.8"/>
        </svg>
        <span>+61 (0) 2 95550417</span>
      </div>
      <div class="contact-row">
        <svg class="contact-icon" viewBox="0 0 24 24" aria-hidden="true">
          <rect x="3" y="2" width="18" height="20" rx="3" fill="#fff"/>
          <rect x="6.5" y="5.5" width="11" height="13" fill="#1c2a7a"/>
          <path d="M8 17 16 7" stroke="#fff" stroke-width="1.5"/>
        </svg>
        <span>+61 (0) 455503862</span>
      </div>
      <div class="contact-row">
        <svg class="contact-icon" viewBox="0 0 24 24" aria-hidden="true">
          <rect x="1" y="1" width="22" height="22" rx="4" fill="#fff"/>
          <text x="12" y="17" text-anchor="middle" font-size="15" font-family="Source Sans 3, sans-serif" fill="#1a1a55">@</text>
        </svg>
        <span>krvconsulting@tallwire.example</span>
      </div>
    </div>
  </div>
</body>
</html>
```